political campaign lawn sign - Governor's Council in Massachuesetts

We are looking for a political lawn sign. We are running a campaign for Governor's Council in Massachusetts. This sign will be on the lawn of homes and businesses so people driving by will see it. It needs to be simple and bold. The last name is long so maybe it could say vote for Marty and then Kolbeck will be big a bold on the next line??
We need it to say:
Vote for Martin Kolbeck
Governor's Council.

Target Market(s)

local residents

Industry/Entity Type

Politcal Campaign

Font styles to use
Sans Serif
Other font styles liked:
• not sure what font but a modern looking one such as Helvetica, Arial, Sans Seri, sharp sans..

Colors
0054AA
0677BA
7BADD7
CADEEF
E8F1F8
00AB8E
00BBA5
67D7C9
C6EFE9
E9F9F6
FFF300
FFF600
FEFA6F
FFFEC7
FFFEE8

Requirements
Must have
• My name written out with a Capital D and R but lower case for every other letter so its Marty Kolbeck
Nice to have
• modern font , the Colors of the lawn sign should have Blue, Yellow and White something bold that will stand out
Should not have
• any maps of Massachusetts

```html
<!DOCTYPE html>
<html lang="en">
<head>
<meta charset="utf-8">
<title>Vote for Marty Kolbeck – Governor's Council lawn sign</title>
<link rel="stylesheet" href="https://fonts.googleapis.com/css2?family=Barlow+Condensed:ital,wght@1,700&family=Roboto:wght@900&family=Montserrat:wght@600&display=swap">
<style>
  :root {
    --sign-blue: #1455a8;
    --star-blue: #0677ba;
    --sign-yellow: #f7ef22;
    --sign-white: #ffffff;
    --page-bg: #e8f1f8;
  }
  html, body {
    margin: 0;
    padding: 0;
    width: 863px;
    height: 1200px;
    overflow: hidden;
    background: var(--page-bg);
  }
  .lawn-sign {
    position: absolute;
    left: 0;
    top: 313px;
    width: 863px;
    height: 575px;
    display: block;
  }
  .sign-field { fill: var(--sign-blue); }
  .sign-frame { fill: none; stroke: var(--sign-white); stroke-width: 3; }
  .office-band { fill: var(--sign-yellow); }
  .accent-star { fill: var(--star-blue); }
  .call-to-vote {
    font-family: "Barlow Condensed", "Arial Narrow", sans-serif;
    font-weight: 700;
    font-style: italic;
    font-size: 118px;
    fill: var(--sign-yellow);
  }
  .first-name {
    font-family: "Barlow Condensed", "Arial Narrow", sans-serif;
    font-weight: 700;
    font-style: italic;
    font-size: 160px;
    fill: var(--sign-white);
  }
  .last-name {
    font-family: "Roboto", Arial, sans-serif;
    font-weight: 900;
    font-size: 206px;
    fill: var(--sign-white);
  }
  .office-title {
    font-family: "Roboto", Arial, sans-serif;
    font-weight: 900;
    font-size: 72px;
    fill: var(--sign-blue);
  }
  .campaign-url {
    font-family: "Montserrat", Arial, sans-serif;
    font-weight: 600;
    font-size: 62px;
    fill: var(--sign-white);
  }
</style>
</head>
<body>
  <svg class="lawn-sign" viewBox="0 0 863 575" role="img" aria-label="Vote for Marty Kolbeck, Governor's Council, voteformarty.net">
    <rect class="sign-field" x="0" y="0" width="863" height="575"/>
    <rect class="sign-frame" x="15" y="15" width="833" height="545"/>
    <g class="star-cluster">
      <polygon class="accent-star" transform="translate(777 68) rotate(12) scale(38)" points="0,-1 0.235,-0.324 0.951,-0.309 0.38,0.124 0.588,0.809 0,0.4 -0.588,0.809 -0.38,0.124 -0.951,-0.309 -0.235,-0.324"/>
      <polygon class="accent-star" transform="translate(700 120) rotate(-8) scale(38)" points="0,-1 0.235,-0.324 0.951,-0.309 0.38,0.124 0.588,0.809 0,0.4 -0.588,0.809 -0.38,0.124 -0.951,-0.309 -0.235,-0.324"/>
      <polygon class="accent-star" transform="translate(797 160) rotate(10) scale(38)" points="0,-1 0.235,-0.324 0.951,-0.309 0.38,0.124 0.588,0.809 0,0.4 -0.588,0.809 -0.38,0.124 -0.951,-0.309 -0.235,-0.324"/>
    </g>
    <text class="call-to-vote" x="43" y="152" textLength="285" lengthAdjust="spacingAndGlyphs">Vote for</text>
    <text class="first-name" x="340" y="192" textLength="300" lengthAdjust="spacingAndGlyphs">Marty</text>
    <text class="last-name" x="37" y="336" textLength="789" lengthAdjust="spacingAndGlyphs">Kolbeck</text>
    <rect class="office-band" x="0" y="370" width="863" height="88"/>
    <text class="office-title" x="40" y="440" textLength="786" lengthAdjust="spacingAndGlyphs">GOVERNOR'S COUNCIL</text>
    <text class="campaign-url" x="176" y="537" textLength="513" lengthAdjust="spacingAndGlyphs">voteformarty.net</text>
  </svg>
</body>
</html>
```